Brantley Water Taxi and Transport

Need to redesign our business cards to relay that we do freight logistics and water taxi service. We also work with gov. agencies doing environmental clean up, oil spill response, remote site construction and work with many of the air taxi and helicopter services on BRANTLEY Island. Out website is www.brantleywatertaxi-example.com to get a better idea of what we do.

Contact Information for Business Card

I have a previous business card but it just has the logo on the front, and a sunset picture on the back with the contact info. It does not relay what we do and what we can help with. I like a simple straight forward design over a busy one.

Colors
3176b5
0455a3
cfdfed

Requirements
Must have
• logo, email, website, phone number

```html
<!DOCTYPE html>
<html lang="en">
<head>
<meta charset="utf-8">
<title>Brantley Water Taxi and Transport – Business Cards</title>
<link href="https://fonts.googleapis.com/css2?family=Questrial&display=swap" rel="stylesheet">
<style>
  :root {
    --stage: #2b2f35;
    --card-paper: #f1f8f0;
    --navy: #1f3a64;
    --stripe: #4f82b2;
    --brand-blue: #0455a3;
    --sun: #f08a1a;
    --alert-red: #e0262b;
    --ink-white: #ffffff;
  }
  html, body {
    margin: 0;
    width: 1200px;
    height: 900px;
    overflow: hidden;
    background: var(--stage);
    font-family: "Questrial", sans-serif;
  }
  .stage {
    position: relative;
    width: 1200px;
    height: 900px;
  }
  .business-card {
    position: absolute;
    left: 250px;
    width: 700px;
    height: 400px;
    box-shadow: 0 14px 30px rgba(0,0,0,0.45);
  }
  .card-contact { top: 40px; }
  .card-brand { top: 470px; }
  .business-card svg { display: block; width: 700px; height: 400px; }
  .business-card text { font-family: "Questrial", sans-serif; }
  .brand-name { letter-spacing: 2px; }
</style>
</head>
<body>
<main class="stage">

  <section class="business-card card-contact" aria-label="Business card, contact side">
    <svg viewBox="0 0 700 400" xmlns="http://www.w3.org/2000/svg">
      <defs>
        <linearGradient id="scene-fill" x1="0" y1="0" x2="1" y2="1">
          <stop offset="0" stop-color="#8fcdec"/>
          <stop offset="0.6" stop-color="#3f8fc4"/>
          <stop offset="1" stop-color="#f4b26b"/>
        </linearGradient>
      </defs>
      <rect class="card-paper" width="700" height="400" fill="var(--card-paper)"/>
      <polygon class="navy-panel" points="0,0 470,0 360,400 0,400" fill="var(--navy)"/>
      <polygon class="white-band" points="0,334 215,334 190,360 0,360" fill="var(--card-paper)"/>
      <g class="accent-stripes" fill="var(--stripe)">
        <polygon points="215,334 260,334 238,360 190,360"/>
        <polygon points="262,334 300,334 282,356 244,356"/>
        <polygon points="222,372 266,372 252,388 208,388"/>
        <polygon points="272,372 316,372 300,390 258,390"/>
      </g>

      <text class="brand-name" x="40" y="64" font-size="44" fill="var(--ink-white)">BRANTLEY</text>
      <text class="brand-tagline" x="42" y="92" font-size="16" fill="var(--ink-white)">Water Taxi &amp; Transport</text>

      <g class="icon-phone" transform="translate(40,126)" fill="none" stroke="var(--alert-red)" stroke-width="3" stroke-linecap="round">
        <path d="M6 2 C2 6 2 16 10 22 M6 2 L10 6 M10 22 L14 18"/>
      </g>
      <g class="icon-mail" transform="translate(34,168)">
        <rect width="26" height="18" fill="var(--alert-red)"/>
        <path d="M0 0 L13 10 L26 0" fill="none" stroke="var(--ink-white)" stroke-width="2"/>
      </g>
      <g class="icon-web" transform="translate(47,220)" fill="none" stroke="var(--alert-red)" stroke-width="2.5">
        <circle r="12"/>
        <ellipse rx="5" ry="12"/>
        <line x1="-12" y1="0" x2="12" y2="0"/>
      </g>
      <line class="icon-divider" x1="80" y1="118" x2="80" y2="242" stroke="var(--ink-white)" stroke-width="2"/>

      <text class="contact-phone" x="98" y="146" font-size="18" fill="var(--ink-white)">555-014-2290</text>
      <text class="contact-email" x="98" y="186" font-size="14" fill="var(--ink-white)">BRANTLEYWATERTAXI@EXAMPLE.COM</text>
      <text class="contact-web" x="98" y="228" font-size="16" fill="var(--ink-white)">www.brantleywatertaxi-example.com</text>

      <text class="slogan" x="40" y="306" font-size="20" fill="var(--ink-white)">The Right Vessel For The Right Job</text>

      <rect class="vessel-scene" x="490" y="100" width="175" height="190" rx="6" fill="url(#scene-fill)" role="img" aria-label="Illustration of a water taxi vessel on waves in front of mountains and a setting sun"/>
    </svg>
  </section>

  <section class="business-card card-brand" aria-label="Business card, brand side">
    <svg viewBox="0 0 700 400" xmlns="http://www.w3.org/2000/svg">
      <rect class="card-paper" width="700" height="400" fill="var(--card-paper)"/>
      <polygon class="navy-edge" points="0,0 24,0 24,312 250,312 310,400 0,400" fill="var(--navy)"/>
      <g class="accent-stripes" fill="var(--stripe)">
        <polygon points="250,312 300,312 330,352 280,352"/>
        <polygon points="312,312 360,312 392,352 344,352"/>
        <polygon points="336,360 384,360 400,382 352,382"/>
      </g>

      <g class="brand-lockup">
        <circle class="brand-dot" cx="244" cy="186" r="14" fill="var(--sun)"/>
        <text class="brand-name" x="270" y="202" font-size="46" fill="var(--brand-blue)">BRANTLEY</text>
        <text class="brand-tagline" x="272" y="232" font-size="17" fill="var(--navy)">Water Taxi &amp; Transport</text>
      </g>
    </svg>
  </section>

</main>
</body>
</html>
```